Brisk Telecom Branding and Visual Identity Project

We need some visual identity items for Brisk Telecom, which should be produced based on the company's logo attached.

I would like the brochure to be as lightweight as possible so that it can be sent via email.

Below are the items we need to be made.

- Company letterhead
- Company brochure in PDF format (single page)
- Email signature (only one)
- Wallpaper
- Banner for use on social media
- Customized shirt

Target Market(s)

Passengers and crew members of ships

Industry/Entity Type

Telecom & Maritime

Colors
0054AA
0677BA
7BADD7
CADEEF
E8F1F8

Requirements
Nice to have
• Colors that match the logo
Should not have
• Colors that clash with the logo colors

```html
<!DOCTYPE html>
<html lang="en">
<head>
<meta charset="utf-8">
<title>Brisk Telecom Letterhead</title>
<link href="https://fonts.googleapis.com/css2?family=Arimo:wght@400&family=Mulish:wght@700&family=Open+Sans:wght@400&display=swap" rel="stylesheet">
<style>
  :root {
    --backdrop: #9b9b9b;
    --paper: #ffffff;
    --brand-blue: #0073bd;
    --rule-grey: #a8a8a8;
    --band-grey: #b3b3b3;
    --text-grey: #555555;
    --meta-grey: #6f6f6f;
  }
  html, body {
    margin: 0;
    padding: 0;
    width: 1033px;
    height: 1200px;
    overflow: hidden;
    background: var(--backdrop);
  }
  .letterhead {
    position: absolute;
    left: 174px;
    top: 116px;
    width: 685px;
    height: 969px;
    background: var(--paper);
    overflow: hidden;
    font-family: "Arimo", Arial, sans-serif;
    color: var(--text-grey);
  }
  .brand {
    position: absolute;
    left: 48px;
    top: 62px;
    display: flex;
    align-items: center;
    gap: 10px;
    font-family: "Mulish", sans-serif;
    font-weight: 700;
    font-size: 30px;
    color: var(--brand-blue);
    letter-spacing: 0.5px;
  }
  .brand-dot {
    width: 18px;
    height: 18px;
    border-radius: 50%;
    background: var(--brand-blue);
  }
  .header-rule {
    position: absolute;
    left: 48px;
    top: 129px;
    width: 589px;
    height: 1px;
    background: var(--rule-grey);
  }
  .contact {
    position: absolute;
    left: 514px;
    top: 50px;
    font-size: 10.5px;
    line-height: 13px;
    color: var(--meta-grey);
  }
  .contact .address { margin-bottom: 6px; }
  .contact .line { display: flex; align-items: center; gap: 7px; }
  .contact svg { width: 8px; height: 8px; flex: none; }
  .salutation {
    position: absolute;
    left: 62px;
    top: 297px;
    margin: 0;
    font-family: "Mulish", sans-serif;
    font-weight: 700;
    font-size: 15.5px;
    color: var(--text-grey);
  }
  .body-copy {
    position: absolute;
    left: 61px;
    top: 342px;
    width: 564px;
    font-size: 11.2px;
    line-height: 14.1px;
  }
  .body-copy p { margin: 0 0 12px; }
  .closing {
    position: absolute;
    left: 62px;
    top: 632px;
    margin: 0;
    font-family: "Mulish", sans-serif;
    font-weight: 700;
    font-size: 9px;
  }
  .signature {
    position: absolute;
    left: 79px;
    top: 678px;
    margin: 0;
    font-family: "Open Sans", sans-serif;
    font-size: 16px;
    letter-spacing: -1px;
    color: #4a4a4a;
  }
  .footer-waves {
    position: absolute;
    left: 0;
    top: 0;
    width: 685px;
    height: 969px;
  }
</style>
</head>
<body>
  <main class="letterhead">
    <div class="brand"><span class="brand-dot"></span>Brisk Telecom</div>

    <address class="contact" style="font-style:normal">
      <div class="address">Your address, city<br>state, ZIP 0000</div>
      <div class="line">
        <svg viewBox="0 0 10 10" aria-hidden="true"><path d="M2 1 L4 1 L4.6 3.2 L3.4 4 Q4.5 6 6 6.6 L6.8 5.4 L9 6 L9 8 Q8.5 9 7.5 9 Q1 8 1 2.5 Q1 1 2 1 Z" fill="var(--brand-blue)"/></svg>
        123-456-2100
      </div>
      <div class="line">
        <svg viewBox="0 0 10 10" aria-hidden="true"><rect x="0.5" y="2" width="9" height="6.5" fill="var(--brand-blue)"/><path d="M0.5 2 L5 5.6 L9.5 2" fill="none" stroke="#fff" stroke-width="0.9"/></svg>
        youremail@example.com
      </div>
      <div class="line">
        <svg viewBox="0 0 10 10" aria-hidden="true"><circle cx="5" cy="5" r="4.3" fill="var(--brand-blue)"/><path d="M1 5 H9 M5 0.7 Q2.5 5 5 9.3 M5 0.7 Q7.5 5 5 9.3" fill="none" stroke="#fff" stroke-width="0.7"/></svg>
        www.yourwebsite.com
      </div>
    </address>

    <div class="header-rule"></div>

    <h1 class="salutation">Dear Mr. Smith,</h1>

    <section class="body-copy">
      <p>Lorem ipsum dolor sit amet, consectetuer adipiscing elit, sed diam nonmmy nibh euismod tincidunt ut laor eet dolore magna aliquam erat volutpat. Ut wisi enim ad minim veniam, quis nostrud exerci tationmcorper suscipit lobortis nisl ut aliquip ex ea commodo consequat. Duis autem vel eum iriure dolor in hendrerit in vulputate velit esse molestie consequat, vel illum dolore eu feugiat</p>
      <p>Rorem ipsum dolor sit amet, consectetuer adipiscing elit, sed diam nonmmy nibh euismod tincidunt ut laor eet dolore magna aliquam erat volutpat. Ut wisi enim ad minim veniam, quis nostrud exerci tationmcorper suscipit lobortis nisl ut aliquip ex ea commodo consequat. Duis autem vel eum iriure dolor in hendrerit in vulputate velit esse molest</p>
      <p>Dorem ipsum dolor sit amet, consectetuer adipiscing elit, sed diam nonmmy nibh euismod tincidunt ut laor eet dolore magna aliquam erat volutpat. Ut wisi enim ad minim veniam, quis nostrud exerci tationmcorper suscipit lobortis nisl ut aliquip ex ea commodo consequat. Duis autem vel eum iriure dolor in hendrerit in suscipit lobortis nisl ut aliquip ex ea commodo consequat. Duis autem vel eum iriure dolor in hendrerit in vulputate velit esse molestie consequat, vel illum</p>
      <p>Sorem ipsum dolor sit amet, consectetuer adipiscing elit, sed diam nonmmy nibh euismod tincidunt ut laor eet dolore magna aliquam erat volutpat. Ut wisi enim ad minim veniam, quis nostrud exerci tationmcorper suscipit lobortis nisl ut aliquip ex ea commodo consequat. Duis autem vel eum iriure dolor in</p>
    </section>

    <p class="closing">Sincerely,</p>
    <p class="signature">Marten Holloway</p>

    <svg class="footer-waves" viewBox="0 0 685 969" aria-hidden="true">
      <path d="M110 938 Q420 962 685 882 L685 901 Q420 970 110 938 Z" fill="var(--band-grey)"/>
      <path d="M0 929 Q300 985 685 908 L685 969 L0 969 Z" fill="var(--brand-blue)"/>
    </svg>
  </main>
</body>
</html>
```